NorthPlain Bytes Yellow rose letterhead

I have a new logo for my company but in its current form it is too large to be used on letterhead or as a email signature. I need to have the designer use elements from the current logo and create something close to the original but more suited for smaller items.
Updates

I just uploaded a copy of our logo that does not have the weathered affect. Thanks

Industry/Entity Type

It Company

Requirements
Must have
• The design must maintain the visual effect of the current logo. It needs to include the yellow rose and the name of the company.
Nice to have
• It would be nice to maintain the stamp theme and incorporate my name, address, phone, email. etc.

```html
<!DOCTYPE html>
<html lang="en">
<head>
<meta charset="utf-8">
<title>NorthPlain Bytes Letterhead</title>
<link rel="stylesheet" href="https://fonts.googleapis.com/css2?family=Montserrat:wght@700;800&display=swap">
<style>
  :root {
    --page: #ffffff;
    --stamp-yellow: #fde699;
    --stamp-light: #fff3c4;
    --perforation-line: #c4c4c4;
    --panel-center: #bcb3a3;
    --panel-edge: #bea678;
    --brand-teal: #7fd0dc;
    --rule: #6e6456;
    --tagline: #ffffff;
    --contact: #8c8272;
    --rose-light: #ffe36a;
    --rose-deep: #e6a91c;
    --rose-leaf: #3fb3b8;
  }
  * { margin: 0; padding: 0; box-sizing: border-box; }
  html, body { width: 1191px; height: 1200px; overflow: hidden; background: var(--page); }
  .letterhead { position: relative; width: 1191px; height: 1200px; font-family: "Montserrat", sans-serif; }
  .stamp-frame { position: absolute; inset: 0; }
  .rose {
    position: absolute; border-radius: 50%;
    background: radial-gradient(circle at 45% 42%, var(--rose-light) 0%, var(--rose-deep) 70%, var(--rose-leaf) 100%);
  }
  .rose--top { left: 57px; top: 80px; width: 125px; height: 125px; }
  .rose--bottom { left: 577px; top: 1005px; width: 126px; height: 126px; }
  .masthead { position: absolute; left: 196px; top: 74px; width: 497px; text-align: center; }
  .brand-name {
    color: var(--brand-teal); font-weight: 800; font-size: 36px; line-height: 34px;
    letter-spacing: 1px;
  }
  .brand-rule { height: 3px; background: var(--rule); margin: 8px 0 6px; }
  .brand-motto { color: var(--tagline); font-weight: 700; font-size: 22px; letter-spacing: 2.5px; line-height: 24px; }
  .brand-promise { color: var(--tagline); font-weight: 700; font-size: 18px; letter-spacing: 1.2px; line-height: 21px; }
  .contact {
    position: absolute; left: 55px; top: 1020px; color: var(--contact);
    font-weight: 800; font-size: 20px; line-height: 20.5px; list-style: none;
  }
</style>
</head>
<body>
<main class="letterhead">
  <svg class="stamp-frame" width="1191" height="1200" viewBox="0 0 1191 1200" aria-hidden="true">
    <defs>
      <linearGradient id="stampFill" x1="0" y1="0" x2="1" y2="1">
        <stop offset="0" stop-color="var(--stamp-yellow)"/>
        <stop offset="0.5" stop-color="var(--stamp-light)"/>
        <stop offset="1" stop-color="var(--stamp-yellow)"/>
      </linearGradient>
      <radialGradient id="panelFill" cx="0.45" cy="0.5" r="0.65">
        <stop offset="0.3" stop-color="var(--panel-center)"/>
        <stop offset="1" stop-color="var(--panel-edge)"/>
      </radialGradient>
    </defs>
    <rect x="0" y="23" width="768" height="1165" fill="url(#stampFill)"/>
    <g class="perforations" fill="var(--page)" stroke="var(--perforation-line)" stroke-width="2">
      <ellipse cx="52" cy="23" rx="23" ry="30"/><ellipse cx="110" cy="23" rx="23" ry="30"/>
      <ellipse cx="168" cy="23" rx="23" ry="30"/><ellipse cx="226" cy="23" rx="23" ry="30"/>
      <ellipse cx="284" cy="23" rx="23" ry="30"/><ellipse cx="342" cy="23" rx="23" ry="30"/>
      <ellipse cx="400" cy="23" rx="23" ry="30"/><ellipse cx="458" cy="23" rx="23" ry="30"/>
      <ellipse cx="516" cy="23" rx="23" ry="30"/><ellipse cx="574" cy="23" rx="23" ry="30"/>
      <ellipse cx="632" cy="23" rx="23" ry="30"/><ellipse cx="690" cy="23" rx="23" ry="30"/>
      <ellipse cx="52" cy="1188" rx="23" ry="30"/><ellipse cx="110" cy="1188" rx="23" ry="30"/>
      <ellipse cx="168" cy="1188" rx="23" ry="30"/><ellipse cx="226" cy="1188" rx="23" ry="30"/>
      <ellipse cx="284" cy="1188" rx="23" ry="30"/><ellipse cx="342" cy="1188" rx="23" ry="30"/>
      <ellipse cx="400" cy="1188" rx="23" ry="30"/><ellipse cx="458" cy="1188" rx="23" ry="30"/>
      <ellipse cx="516" cy="1188" rx="23" ry="30"/><ellipse cx="574" cy="1188" rx="23" ry="30"/>
      <ellipse cx="632" cy="1188" rx="23" ry="30"/><ellipse cx="690" cy="1188" rx="23" ry="30"/>
      <ellipse cx="0" cy="85" rx="28" ry="42"/><ellipse cx="0" cy="200" rx="28" ry="42"/>
      <ellipse cx="0" cy="315" rx="28" ry="42"/><ellipse cx="0" cy="430" rx="28" ry="42"/>
      <ellipse cx="0" cy="545" rx="28" ry="42"/><ellipse cx="0" cy="660" rx="28" ry="42"/>
      <ellipse cx="0" cy="775" rx="28" ry="42"/><ellipse cx="0" cy="890" rx="28" ry="42"/>
      <ellipse cx="0" cy="1005" rx="28" ry="42"/><ellipse cx="0" cy="1120" rx="28" ry="42"/>
      <ellipse cx="768" cy="85" rx="28" ry="42"/><ellipse cx="768" cy="200" rx="28" ry="42"/>
      <ellipse cx="768" cy="315" rx="28" ry="42"/><ellipse cx="768" cy="430" rx="28" ry="42"/>
      <ellipse cx="768" cy="545" rx="28" ry="42"/><ellipse cx="768" cy="660" rx="28" ry="42"/>
      <ellipse cx="768" cy="775" rx="28" ry="42"/><ellipse cx="768" cy="890" rx="28" ry="42"/>
      <ellipse cx="768" cy="1005" rx="28" ry="42"/><ellipse cx="768" cy="1120" rx="28" ry="42"/>
    </g>
    <rect x="46" y="63" width="672" height="1074" fill="url(#panelFill)"/>
  </svg>

  <div class="rose rose--top" role="img" aria-label="Yellow rose illustration"></div>

  <header class="masthead">
    <h1 class="brand-name">NorthPlain<br>Bytes</h1>
    <div class="brand-rule"></div>
    <p class="brand-motto">PRECISION DATA STUDIO</p>
    <p class="brand-promise">Building Clear, Reliable<br>Audience Insight for Every Team</p>
  </header>

  <ul class="contact">
    <li>Vera Holloway, PhD</li>
    <li>214 W Prairie Line Rd, STE 1180</li>
    <li>Dalton Springs, TX 75990</li>
    <li>vera@northplain-bytes.com</li>
    <li>1-800-555-0147</li>
  </ul>

  <div class="rose rose--bottom" role="img" aria-label="Yellow rose illustration"></div>
</main>
</body>
</html>
```